Velorin Banner Design

We need banners for new company Velorin Holdings Limited located in Hong Kong. Velorin is an global online business platform, needs clean white, blue and red color mix banners.

Reason: I am extending for final design

Target Market(s)

Velorin an online Business Company have a target home based business owners and DIY website seekers.

Industry/Entity Type

Business

Colors
0355a3
ec2027
ffffff

Requirements
Must have
• Free Sign Up Button and Velorin Logo

```html
<!DOCTYPE html>
<html lang="en">
<head>
<meta charset="utf-8">
<title>Velorin Banner Set</title>
<link rel="stylesheet" href="https://fonts.googleapis.com/css2?family=Arimo:ital,wght@0,400;0,700;1,700&display=swap">
<style>
  :root{
    --brand-blue:#0355a3;
    --brand-blue-deep:#023d77;
    --brand-blue-light:#2a86d6;
    --brand-red:#ec2027;
    --brand-red-deep:#b8141a;
    --white:#ffffff;
    --soft-white:#f1f5fa;
    --ink:#1a1a1a;
    --logo-ink:#0355a3;
    --size-accent:#ec2027;
    --photo-a:#dfe8f3;
    --photo-b:#a8c1dc;
  }
  *{box-sizing:border-box;margin:0;padding:0}
  html,body{width:1200px;height:1200px;overflow:hidden;background:var(--white)}
  body{position:relative;font-family:"Arimo",Arial,sans-serif}

  .banner{position:absolute;overflow:hidden;border:1px solid var(--brand-blue-deep);background:var(--brand-blue)}
  .top{position:absolute;left:0;right:0;top:0;background:linear-gradient(var(--brand-blue),var(--brand-blue-deep))}
  .heading{color:var(--white);font-weight:700;text-align:center;line-height:1.1}
  .heading.italic{font-style:italic}
  .band{position:absolute;left:0;right:0;background:linear-gradient(var(--brand-blue-light),var(--brand-blue))}
  .band-text{color:var(--white);font-weight:700;text-align:center;line-height:1.15}
  .band-text .light{font-weight:400;display:block}
  .accent-line{position:absolute;left:0;right:0;height:5px;background:var(--brand-red)}
  .action{position:absolute;left:0;right:0;bottom:0;background:linear-gradient(var(--white),var(--soft-white))}
  .earn{color:var(--brand-blue);font-weight:700;text-align:center;line-height:1.05}
  .arc{position:absolute;left:0;width:100%}
  .photo-panel{position:absolute;background:var(--white);border-radius:14px;overflow:hidden;box-shadow:0 1px 3px rgba(0,0,0,.3)}
  .photo{position:absolute;background:radial-gradient(ellipse at 40% 45%,var(--photo-a),var(--photo-b) 75%)}
  .logo-name{position:absolute;color:var(--logo-ink);font-weight:700;letter-spacing:.5px;white-space:nowrap}
  .free-tag{position:absolute;color:var(--brand-red);font-weight:700}

  .btn{position:absolute;border-radius:5px;overflow:hidden;background:linear-gradient(var(--brand-red),var(--brand-red-deep));box-shadow:0 1px 2px rgba(0,0,0,.4)}
  .btn-label{position:absolute;top:0;bottom:0;display:flex;align-items:center;color:var(--white);font-weight:700;white-space:nowrap}
  .btn-icon{position:absolute;top:50%;transform:translateY(-50%)}
  .ribbon{position:absolute;background:var(--brand-blue);color:var(--white);font-weight:700;text-align:center;transform:rotate(-45deg)}

  .size-label{position:absolute;font-size:21px;color:var(--ink);white-space:nowrap}
  .size-label .weight{color:var(--size-accent);margin-left:8px}

  /* 468 x 60 */
  .b468{left:92px;top:126px;width:661px;height:85px}
  .b468 .top{width:168px;right:auto;height:85px;display:flex;align-items:center;justify-content:center}
  .b468 .heading{font-size:19px}
  .b468 .photo-panel{left:172px;top:5px;width:210px;height:75px;border-radius:16px}
  .b468 .photo{left:0;top:0;width:110px;height:75px}
  .b468 .logo-name{left:118px;top:27px;font-size:18px}
  .b468 .band{left:388px;right:auto;width:108px;top:0;height:85px;display:flex;align-items:center;justify-content:center}
  .b468 .band-text{font-size:15px}
  .b468 .accent-line.vertical{left:496px;top:0;width:5px;height:85px}
  .b468 .action{left:501px;top:0}
  .b468 .earn{font-size:14px;margin-top:5px}
  .b468 .btn{left:10px;top:40px;width:140px;height:38px}
  .b468 .btn-label{left:34px;font-size:17px}
  .b468 .btn-icon{right:7px}
  .b468 .ribbon{left:-22px;top:8px;width:70px;font-size:9px}

  /* 250 x 250 */
  .b250{left:92px;top:295px;width:353px;height:353px}
  .b250 .top{height:80px;padding-top:6px}
  .b250 .heading{font-size:24px}
  .b250 .arc{top:62px;height:40px}
  .b250 .band{top:80px;height:190px}
  .b250 .photo-panel{left:14px;top:75px;width:320px;height:118px;border-radius:18px}
  .b250 .photo{left:14px;top:6px;width:110px;height:106px}
  .b250 .photo.cash{left:250px;top:8px;width:62px;height:100px}
  .b250 .logo-name{left:136px;top:43px;font-size:26px}
  .b250 .band-text{position:absolute;left:0;right:0;top:140px;font-size:18px}
  .b250 .band-text .light{font-size:17px;margin-top:6px}
  .b250 .accent-line{top:268px}
  .b250 .action{top:273px;display:flex;align-items:center}
  .b250 .earn{width:130px;font-size:19px}
  .b250 .btn{left:137px;top:15px;width:200px;height:52px}
  .b250 .btn-label{left:52px;font-size:25px}
  .b250 .btn-icon{right:10px}
  .b250 .ribbon{left:-26px;top:12px;width:90px;font-size:13px}

  /* 125 x 125 */
  .b125{left:563px;top:364px;width:177px;height:177px}
  .b125 .top{height:40px;padding-top:3px}
  .b125 .heading{font-size:13.5px}
  .b125 .arc{top:30px;height:18px}
  .b125 .band{top:40px;height:92px}
  .b125 .photo-panel{left:5px;top:38px;width:167px;height:62px;border-radius:10px}
  .b125 .photo{left:6px;top:3px;width:56px;height:56px}
  .b125 .photo.cash{left:124px;top:4px;width:38px;height:52px}
  .b125 .logo-name{left:68px;top:22px;font-size:12px}
  .b125 .band-text{position:absolute;left:0;right:0;top:68px;font-size:12px}
  .b125 .accent-line{top:130px;height:4px}
  .b125 .action{top:134px}
  .b125 .btn{left:22px;top:4px;width:126px;height:36px}
  .b125 .btn-label{left:32px;font-size:15px}
  .b125 .btn-icon{right:6px}
  .b125 .ribbon{left:-20px;top:6px;width:62px;font-size:9px}

  /* 120 x 160 */
  .b120x160{left:95px;top:772px;width:170px;height:226px}
  .b120x160 .top{height:40px;padding-top:4px}
  .b120x160 .heading{font-size:13.5px}
  .b120x160 .arc{top:30px;height:18px}
  .b120x160 .band{top:40px;height:128px}
  .b120x160 .photo-panel{left:5px;top:38px;width:160px;height:90px;border-radius:10px}
  .b120x160 .photo{left:6px;top:8px;width:66px;height:80px}
  .b120x160 .photo.cash{left:112px;top:36px;width:42px;height:50px}
  .b120x160 .logo-name{left:78px;top:14px;font-size:12px}
  .b120x160 .band-text{position:absolute;left:0;right:0;top:142px;font-size:12px}
  .b120x160 .accent-line{top:166px;height:4px}
  .b120x160 .action{top:170px}
  .b120x160 .btn{left:6px;top:5px;width:156px;height:45px}
  .b120x160 .btn-label{left:44px;font-size:17px}
  .b120x160 .btn-icon{right:9px}
  .b120x160 .ribbon{left:-22px;top:8px;width:70px;font-size:10px}

  /* 120 x 90 */
  .b120x90{left:569px;top:792px;width:170px;height:127px}
  .b120x90 .top{height:38px;padding-top:3px}
  .b120x90 .heading{font-size:13.5px}
  .b120x90 .arc{top:28px;height:18px}
  .b120x90 .band{top:38px;height:89px}
  .b120x90 .photo-panel{left:5px;top:36px;width:160px;height:62px;border-radius:10px}
  .b120x90 .photo{left:6px;top:3px;width:52px;height:56px}
  .b120x90 .photo.cash{left:118px;top:8px;width:36px;height:48px}
  .b120x90 .free-tag{left:68px;top:10px;font-size:14px}
  .b120x90 .logo-name{left:66px;top:32px;font-size:11px}
  .b120x90 .band-text{position:absolute;left:0;right:0;top:68px;font-size:12px}

  /* 160 x 600 */
  .b160{left:884px;top:121px;width:226px;height:847px}
  .b160 .top{height:150px;padding-top:12px}
  .b160 .heading{font-size:27px;line-height:1.1}
  .b160 .arc{top:125px;height:50px}
  .b160 .band{top:150px;height:528px}
  .b160 .photo-panel{left:20px;top:160px;width:188px;height:330px;border-radius:26px}
  .b160 .photo{left:14px;top:12px;width:160px;height:220px}
  .b160 .photo.cash{left:108px;top:170px;width:74px;height:80px}
  .b160 .logo-name{left:0;right:0;top:270px;text-align:center;font-size:30px}
  .b160 .band-text{position:absolute;left:0;right:0;top:355px;font-size:24px;line-height:1.05}
  .b160 .band-text .light{font-size:23px;margin-top:8px}
  .b160 .accent-line{top:676px;height:7px}
  .b160 .action{top:683px}
  .b160 .earn{font-size:28px;margin-top:12px;line-height:1}
  .b160 .btn{left:10px;top:103px;width:205px;height:53px}
  .b160 .btn-label{left:58px;font-size:25px}
  .b160 .btn-icon{right:10px}
  .b160 .ribbon{left:-26px;top:12px;width:92px;font-size:13px}
</style>
</head>
<body>

<div class="banner b468">
  <div class="top"><p class="heading">Revolutionary<br>Single Line<br>Aff. Program</p></div>
  <div class="photo-panel">
    <div class="photo" role="img" aria-label="Photo of a woman sitting with a laptop"></div>
    <span class="logo-name">Velorin</span>
  </div>
  <div class="band"><p class="band-text">Create<br>Your Own<br>Ecommerce<br>site</p></div>
  <div class="accent-line vertical"></div>
  <div class="action">
    <p class="earn">START EARNINGS<br>ONLINE</p>
    <div class="btn">
      <span class="ribbon">FREE</span>
      <span class="btn-label">Sign Up</span>
      <svg class="btn-icon" width="22" height="22" viewBox="0 0 24 24"><circle cx="12" cy="12" r="11" fill="var(--white)"/><path d="M9 6.5 17 12 9 17.5Z" fill="var(--brand-red)"/></svg>
    </div>
  </div>
</div>
<p class="size-label" style="left:314px;top:223px">468X60<span class="weight">14.2kb</span></p>

<div class="banner b250">
  <div class="top"><p class="heading">Revolutionary Single Line<br>Affiliate Program</p></div>
  <div class="band">
    <p class="band-text">Create Your Own Ecommerce site<span class="light">@ minimum $10/Month</span></p>
  </div>
  <svg class="arc" viewBox="0 0 353 40" preserveAspectRatio="none"><path d="M0 30 Q176 -6 353 30 L353 40 Q176 4 0 40Z" fill="var(--brand-red)"/></svg>
  <div class="photo-panel">
    <div class="photo" role="img" aria-label="Photo of a woman sitting with a laptop"></div>
    <span class="logo-name">Velorin</span>
    <div class="photo cash" role="img" aria-label="Photo of a hand holding cash"></div>
  </div>
  <div class="accent-line"></div>
  <div class="action">
    <p class="earn">START<br>EARNINGS<br>ONLINE</p>
    <div class="btn">
      <span class="ribbon">FREE</span>
      <span class="btn-label">Sign Up</span>
      <svg class="btn-icon" width="32" height="32" viewBox="0 0 24 24"><circle cx="12" cy="12" r="11" fill="var(--white)"/><path d="M9 6.5 17 12 9 17.5Z" fill="var(--brand-red)"/></svg>
    </div>
  </div>
</div>
<p class="size-label" style="left:180px;top:657px">250X250<span class="weight">25kb</span></p>

<div class="banner b125">
  <div class="top"><p class="heading italic">Revolutionary Single<br>Line Aff. Program</p></div>
  <div class="band"><p class="band-text">Own your ecommerce</p></div>
  <svg class="arc" viewBox="0 0 177 18" preserveAspectRatio="none"><path d="M0 12 Q88 -3 177 12 L177 18 Q88 3 0 18Z" fill="var(--brand-red)"/></svg>
  <div class="photo-panel">
    <div class="photo" role="img" aria-label="Photo of a woman sitting with a laptop"></div>
    <span class="logo-name">Velorin</span>
    <div class="photo cash" role="img" aria-label="Photo of a hand holding cash"></div>
  </div>
  <div class="accent-line"></div>
  <div class="action">
    <div class="btn">
      <span class="ribbon">FREE</span>
      <span class="btn-label">Sign Up</span>
      <svg class="btn-icon" width="20" height="20" viewBox="0 0 24 24"><circle cx="12" cy="12" r="11" fill="var(--white)"/><path d="M9 6.5 17 12 9 17.5Z" fill="var(--brand-red)"/></svg>
    </div>
  </div>
</div>
<p class="size-label" style="left:582px;top:555px;font-size:19px">125X125<span class="weight">9.6kb</span></p>

<div class="banner b120x160">
  <div class="top"><p class="heading italic">Revolutionary Single<br>Line Aff. Program</p></div>
  <div class="band"><p class="band-text">Own your ecommerce</p></div>
  <svg class="arc" viewBox="0 0 170 18" preserveAspectRatio="none"><path d="M0 12 Q85 -3 170 12 L170 18 Q85 3 0 18Z" fill="var(--brand-red)"/></svg>
  <div class="photo-panel">
    <div class="photo" role="img" aria-label="Photo of a woman sitting with a laptop"></div>
    <span class="logo-name">Velorin</span>
    <div class="photo cash" role="img" aria-label="Photo of a hand holding cash"></div>
  </div>
  <div class="accent-line"></div>
  <div class="action">
    <div class="btn">
      <span class="ribbon">FREE</span>
      <span class="btn-label">Sign Up</span>
      <svg class="btn-icon" width="24" height="24" viewBox="0 0 24 24"><circle cx="12" cy="12" r="11" fill="var(--white)"/><path d="M9 6.5 17 12 9 17.5Z" fill="var(--brand-red)"/></svg>
    </div>
  </div>
</div>
<p class="size-label" style="left:99px;top:1008px;font-size:19px">120X160<span class="weight">10.8kb</span></p>

<div class="banner b120x90">
  <div class="top"><p class="heading italic">Revolutionary Single<br>Line Aff. Program</p></div>
  <div class="band"><p class="band-text">Own your ecommerce</p></div>
  <svg class="arc" viewBox="0 0 170 18" preserveAspectRatio="none"><path d="M0 12 Q85 -3 170 12 L170 18 Q85 3 0 18Z" fill="var(--brand-red)"/></svg>
  <div class="photo-panel">
    <div class="photo" role="img" aria-label="Photo of a woman sitting with a laptop"></div>
    <span class="free-tag">FREE</span>
    <span class="logo-name">Velorin</span>
    <div class="photo cash" role="img" aria-label="Photo of a hand holding cash"></div>
  </div>
</div>
<p class="size-label" style="left:581px;top:929px;font-size:19px">120X90<span class="weight">7.35kb</span></p>

<div class="banner b160">
  <div class="top"><p class="heading">Revolutionary<br>Single Line<br>Affiliate<br>Program</p></div>
  <div class="band">
    <p class="band-text">Create Your<br>Own<br>Ecommerce<br>Website<span class="light">@ minimum<br>$10/Month</span></p>
  </div>
  <svg class="arc" viewBox="0 0 226 50" preserveAspectRatio="none"><path d="M0 30 Q113 -4 226 30 L226 50 Q113 14 0 50Z" fill="var(--brand-red)"/></svg>
  <div class="photo-panel">
    <div class="photo" role="img" aria-label="Photo of a woman sitting with a laptop"></div>
    <div class="photo cash" role="img" aria-label="Photo of a hand holding cash"></div>
    <span class="logo-name">Velorin</span>
  </div>
  <div class="accent-line"></div>
  <div class="action">
    <p class="earn">START<br>EARNINGS<br>ONLINE</p>
    <div class="btn">
      <span class="ribbon">FREE</span>
      <span class="btn-label">Sign Up</span>
      <svg class="btn-icon" width="34" height="34" viewBox="0 0 24 24"><circle cx="12" cy="12" r="11" fill="var(--white)"/><path d="M9 6.5 17 12 9 17.5Z" fill="var(--brand-red)"/></svg>
    </div>
  </div>
</div>
<p class="size-label" style="left:902px;top:982px;font-size:23px">160X600<span class="weight">35.9kb</span></p>

</body>
</html>
```